5th Battalion 41st Armored Regiment " Iron Falcons"

Hello,
I am a lieutenant in the Coastal Union Army and my boss lieutenant colonel (commander) has asked me to come up with a business card for him. I threw a few designs toward him and he declined all of them. He really like the Knight business card background that is attached below(, but would like another Knight to replace it). We are 5th Battalion 41st Armored Regiment (Iron Falcons is are Battalion Symbol) and are a Heavy Armored Combat team( Tanks and Halvorsen's). He is an Infantry LTC would love a Bold but simple Iron Falcon riding on a horse. It doesn’t have to have the same back ground as the attached file named Finished Card, but will need all the information that is on both sides of the card. Thank you very much for your help and I look forward to seeing the designs.
V/R
Dale Merriwick

Reason: My boss would like to see a few more designs.

```html
<!DOCTYPE html>
<html lang="en">
<head>
<meta charset="utf-8">
<title>5th Battalion, 41st Armored Regiment – Battalion Commander Card</title>
<link rel="stylesheet" href="https://fonts.googleapis.com/css2?family=Stardos+Stencil:wght@700&family=Cinzel:wght@400;700&family=Montserrat:wght@500&family=Open+Sans:wght@500&display=swap">
<style>
  :root {
    --paper: #ffffff;
    --camo-deep: #0f2a0c;
    --camo-mid: #2f6a1f;
    --camo-light: #4f8a2c;
    --ink-light: #ffffff;
    --ink-dark: #111111;
    --mark-fill: #1b1f5c;
    --mark-text: #f2e21a;
  }
  * { margin: 0; padding: 0; box-sizing: border-box; }
  html, body { width: 1200px; height: 702px; overflow: hidden; background: var(--paper); }
  .canvas { position: relative; width: 1200px; height: 702px; background: var(--paper); }
  .card {
    position: absolute; left: 24px; top: 20px; width: 1165px; height: 664px;
    overflow: hidden;
  }
  .camo-field {
    position: absolute; inset: 0;
    background:
      radial-gradient(ellipse at 50% 40%, var(--camo-light) 0%, var(--camo-mid) 40%, var(--camo-deep) 100%);
  }
  .unit-title {
    position: absolute; left: 0; right: 0; top: 58px; text-align: center;
    font-family: "Stardos Stencil", "Georgia", serif; font-weight: 700;
    font-size: 34px; letter-spacing: 2px; color: var(--ink-light);
    text-shadow: 2px 2px 3px rgba(0,0,0,.6);
  }
  .unit-title sup { font-size: 18px; vertical-align: 14px; }
  .title-rule {
    position: absolute; left: 98px; top: 108px; width: 967px; height: 3px;
    background: var(--ink-light);
  }
  .unit-nickname {
    position: absolute; left: 0; right: 0; top: 125px; text-align: center;
    font-family: "Cinzel", serif; font-size: 20px; letter-spacing: 12px;
    color: var(--ink-light);
  }
  .name-banner { position: absolute; left: 198px; top: 194px; width: 788px; height: 118px; }
  .role, .person {
    position: absolute; left: 280px;
    font-family: "Montserrat", "Arial", sans-serif; font-weight: 500;
    font-size: 28px; letter-spacing: 1px; color: var(--ink-dark);
  }
  .role { top: 212px; }
  .person { top: 258px; }
  .unit-mark {
    position: absolute; left: 70px; top: 168px; width: 160px; height: 160px;
    background: var(--mark-fill);
    display: flex; align-items: center; justify-content: center; text-align: center;
    font-family: "Cinzel", serif; font-weight: 700; font-size: 22px; line-height: 1.2;
    color: var(--mark-text);
  }
  .address, .phones {
    position: absolute; top: 356px;
    font-family: "Cinzel", serif; font-size: 26px; line-height: 34px; letter-spacing: 1.5px;
    color: var(--ink-light);
  }
  .address { right: 650px; text-align: right; }
  .phones { left: 640px; }
  .divider {
    position: absolute; left: 582px; top: 324px; width: 3px; height: 180px;
    background: var(--ink-light);
  }
  .email {
    position: absolute; left: 0; right: 0; top: 530px; text-align: center;
    font-family: "Open Sans", "Arial", sans-serif; font-weight: 500; font-size: 24px;
    color: var(--ink-light);
  }
</style>
</head>
<body>
<div class="canvas">
  <section class="card">
    <div class="camo-field" role="img" aria-label="Green woodland camouflage pattern background"></div>

    <h1 class="unit-title">5<sup>TH</sup> BATTALION, 41<sup>ST</sup> ARMORED REGIMENT</h1>
    <div class="title-rule"></div>
    <p class="unit-nickname">IRON FALCONS</p>

    <svg class="name-banner" viewBox="0 0 788 118" aria-hidden="true">
      <defs>
        <filter id="banner-shadow" x="-5%" y="-20%" width="110%" height="150%">
          <feDropShadow dx="2" dy="4" stdDeviation="3" flood-color="#000" flood-opacity=".5"/>
        </filter>
      </defs>
      <polygon points="0,0 630,0 765,110 0,110" fill="#ffffff" filter="url(#banner-shadow)"/>
    </svg>
    <p class="role">BATTALION COMMANDER</p>
    <p class="person">MARCUS T. ELLERY</p>

    <div class="unit-mark">IRON<br>FALCONS</div>

    <address class="address" style="font-style:normal">
      2285 Garrison Rd.<br>Fort Calder<br>KS 66519
    </address>
    <div class="divider"></div>
    <p class="phones">
      Work : 785-555-0143<br>BB : 785-555-0178<br>Cell : 253-555-0192
    </p>

    <p class="email">marcus.t.ellery.mil@mail.example</p>
  </section>
</div>
</body>
</html>
```